Wine Bottle Label for Cora Whitlow California Wine

This will be a wine bottle label. The wine is produced from grapes from our family farm. Images at bottom are some of same ones in high resolution

Cora Whitlow
Reserve Pinot Noir
Clarksburg 2023
Estate Grown (in cursive)

We would like to have a view from above, looking down from the levee there is a slough (wing of a river) running behind it, it looks down over vineyards, a big wood barn, a giant Oak Tree beyond the barn. There are beautiful sunsets there in the distance. Many birds fly over the vineyards including small black birds (as shown in one photo). Please use what you can from these suggestions to make a label. We will need a small image for back label and wording on it.

Other font styles liked:
• Wine bottle fonts

Requirements
Must have
• Wording mentioned . An Oak Tree with images of the vines and a sunset
Nice to have
• Flock of black birds flying in the sky

```html
<!DOCTYPE html>
<html lang="en">
<head>
<meta charset="utf-8">
<title>Cora Whitlow – Reserve Pinot Noir Label</title>
<link rel="stylesheet" href="https://fonts.googleapis.com/css2?family=Playfair+Display:wght@400&family=Tinos&family=Source+Sans+3:wght@400&family=Arimo:ital@1&display=swap">
<style>
  :root {
    --page: #fefefe;
    --label: #f5f5f5;
    --teal: #3f6469;
    --olive: #8a9a4b;
    --olive-dark: #56621f;
    --ink: #111111;
  }
  * { margin: 0; padding: 0; box-sizing: border-box; }
  html, body {
    width: 1200px;
    height: 1200px;
    overflow: hidden;
    background: var(--page);
  }
  .canvas {
    position: relative;
    width: 1200px;
    height: 1200px;
  }
  .label {
    position: absolute;
    left: 350px;
    top: 144px;
    width: 538px;
    height: 817px;
    background: var(--label);
    overflow: hidden;
  }
  .oak-artwork {
    position: absolute;
    left: 47px;
    top: 61px;
    width: 438px;
    height: 397px;
  }
  .brand-name {
    position: absolute;
    left: 0;
    width: 100%;
    top: 500px;
    text-align: center;
    font-family: "Playfair Display", "Bodoni Moda", serif;
    font-weight: 400;
    font-size: 56px;
    line-height: 1;
    letter-spacing: 0.13em;
    padding-left: 0.13em;
    color: var(--teal);
    white-space: nowrap;
  }
  .varietal {
    position: absolute;
    left: 56px;
    width: 414px;
    top: 622px;
    display: flex;
    align-items: center;
    justify-content: space-between;
    gap: 10px;
  }
  .varietal-rule {
    flex: 0 0 47px;
    height: 2px;
    background: var(--olive);
  }
  .varietal-name {
    font-family: "Tinos", "Times New Roman", serif;
    font-weight: 400;
    font-size: 27px;
    line-height: 1;
    color: var(--olive);
    white-space: nowrap;
  }
  .appellation {
    position: absolute;
    left: 0;
    width: 100%;
    top: 656px;
    text-align: center;
    font-family: "Source Sans 3", "Myriad Pro", sans-serif;
    font-weight: 400;
    font-size: 25px;
    line-height: 1;
    color: var(--olive-dark);
  }
  .estate-note {
    position: absolute;
    left: 0;
    width: 100%;
    top: 710px;
    text-align: center;
    font-family: "Arimo", Arial, sans-serif;
    font-style: italic;
    font-size: 18px;
    line-height: 1;
    color: var(--ink);
  }
</style>
</head>
<body>
  <main class="canvas">
    <section class="label">
      <svg class="oak-artwork" viewBox="0 0 438 397" role="img" aria-label="Illustration of a broad oak tree with a striped teal trunk and olive green leaves">
        <defs>
          <radialGradient id="canopy-tone" cx="50%" cy="40%" r="60%">
            <stop offset="0%" stop-color="#5a7a5e"/>
            <stop offset="100%" stop-color="#8a9a4b"/>
          </radialGradient>
        </defs>
        <rect width="438" height="397" fill="url(#canopy-tone)"/>
      </svg>

      <h1 class="brand-name">Cora Whitlow</h1>

      <div class="varietal">
        <span class="varietal-rule"></span>
        <h2 class="varietal-name">RESERVE PINOT NOIR</h2>
        <span class="varietal-rule"></span>
      </div>

      <p class="appellation">Clarksburg 2023</p>
      <p class="estate-note">Estate Grown</p>
    </section>
  </main>
</body>
</html>
```